We need a set of stationary to compliment our new logo including letterhead (A4 & A5), envelopes, Business cards and appointment cards.

Hi Designers - our details are set out below.
Ashbrook Family Medical
Shop 7, 23-25 Tolley Parade
BRAMLEY HEIGHTS SA 5190
Phone - 08 84967342
Fax - 08 84967349
www.ashbrookfm-example.com.au

Cheers Meg

Industry/Entity Type

Medical

Requirements
Must have
• Reflect the logo be modern and classy

```html
<!DOCTYPE html>
<html lang="en">
<head>
<meta charset="utf-8">
<title>Envelope – Ashbrook Family Medical</title>
<link href="https://fonts.googleapis.com/css2?family=Open+Sans:wght@400;600&display=swap" rel="stylesheet">
<style>
  :root {
    --board: #d9d9d9;
    --paper: #eeeeee;
    --blue: #1569a6;
    --green: #7db23a;
    --ink: #333333;
    --title: #4a4a4a;
  }
  * { margin: 0; padding: 0; box-sizing: border-box; }
  html, body { width: 1200px; height: 844px; overflow: hidden; }
  body {
    background: radial-gradient(ellipse at 40% 30%, #dedede, var(--board) 70%);
    font-family: "Open Sans", Arial, sans-serif;
    position: relative;
  }
  .board-title {
    position: absolute; top: 80px; left: 0; width: 1215px;
    text-align: center; font-size: 35px; font-weight: 400; color: var(--title);
  }
  .envelope {
    position: absolute; left: 349px; width: 536px; height: 268px;
    background: var(--paper);
    box-shadow: 0 1px 3px rgba(0,0,0,0.25);
    overflow: hidden;
  }
  .envelope-front { top: 179px; }
  .envelope-back { top: 532px; }
  .brand {
    position: absolute; left: 24px; top: 69px;
    display: flex; align-items: center; gap: 6px;
  }
  .brand-mark { width: 10px; height: 10px; border-radius: 50%; background: var(--green); }
  .brand-name {
    font-size: 19px; line-height: 24px; font-weight: 400; color: var(--blue); letter-spacing: 0.2px;
  }
  .return-rule {
    position: absolute; left: 0; top: 213px; width: 192px; height: 1px; background: var(--green);
  }
  .return-address {
    position: absolute; left: 24px; top: 221px;
    font-style: normal; font-size: 6.9px; line-height: 9.5px; color: var(--ink);
    white-space: nowrap;
  }
  .return-address .org { font-weight: 600; }
  .return-address .web { color: var(--blue); }
  .base-band {
    position: absolute; left: 0; bottom: 0; width: 100%; height: 10px;
    display: flex;
  }
  .base-band .blue { width: 302px; background: var(--blue); }
  .base-band .green { flex: 1; background: var(--green); }
  .flap {
    position: absolute; top: 0; left: 0; width: 100%; height: 81px;
    background: var(--blue); border-radius: 0 0 21px 21px;
  }
</style>
</head>
<body>
  <h1 class="board-title">Envelope</h1>

  <section class="envelope envelope-front" aria-label="Envelope front">
    <div class="brand">
      <span class="brand-mark"></span>
      <span class="brand-name">ASHBROOK</span>
    </div>
    <div class="return-rule"></div>
    <address class="return-address">
      <div class="org">Ashbrook Family Medical</div>
      <div>Shop 7, 23-25 Tolley Parade BRAMLEY HEIGHTS SA 5190</div>
      <div class="web">www.ashbrookfm-example.com.au</div>
    </address>
    <div class="base-band"><span class="blue"></span><span class="green"></span></div>
  </section>

  <section class="envelope envelope-back" aria-label="Envelope back">
    <div class="flap"></div>
  </section>
</body>
</html>
```